Packaging designed for both the bar and the box for retail and online sales

The name of the product is Plum Crumb. We manufacture a consumer package good product that's a healthy edible cookie dough bar. The product look, feels and tastes like cookie dough. It's sold in the refrigerator section of retail stores next to cookie dough and golden slab. The product is Gluten Free, Diary Free and include B-12, Biotin and Collagen. The ingredients are natural. When design this think about who eat cookie dough and how to engage the buyer in purchasing the product.

We needs design packaging designed for both the bar and the box. I have attached the die lines for both products.

Target Market(s)

Our customer is 16-45. Primarily female but really anyone. Middle to upper income. Interest include healthy life style and yoga. Like to eat something sweet but not feel guilty.

Colors

Designer to choose colors to be used in the design.

Requirements
Must have
• Must be clean, warm, inviting. Brand designs I really like are Golden Slab.
Should not have
• Should not have a photo of food

```html
<!DOCTYPE html>
<html lang="en">
<head>
<meta charset="utf-8">
<title>Plum Crumb – Bar Wrapper</title>
<link rel="stylesheet" href="https://fonts.googleapis.com/css2?family=Poppins:wght@700;800&family=Quicksand:wght@600&display=swap">
<style>
  :root {
    --green: #3f8a3c;
    --green-light: #5a9e52;
    --green-pale: #e4efe1;
    --wrapper: #f3f4f3;
    --ink: #2f2f2c;
    --page: #ffffff;
  }
  html, body {
    margin: 0;
    padding: 0;
    width: 1200px;
    height: 1200px;
    overflow: hidden;
    background: var(--page);
  }
  .canvas {
    position: relative;
    width: 1200px;
    height: 1200px;
  }
  .wrapper {
    position: absolute;
    left: 231px;
    top: 373px;
    width: 797px;
    height: 304px;
  }
  .wrapper svg { display: block; }
  .brand-name {
    font-family: "Poppins", sans-serif;
    font-weight: 800;
    fill: var(--green);
    letter-spacing: 1px;
  }
  .flavour {
    font-family: "Quicksand", sans-serif;
    font-weight: 600;
    fill: var(--ink);
    letter-spacing: 2px;
  }
  .badge-label {
    font-family: "Poppins", sans-serif;
    font-weight: 700;
    font-size: 14px;
    fill: var(--green);
  }
</style>
</head>
<body>
<main class="canvas">
  <div class="wrapper">
    <svg width="797" height="304" viewBox="0 0 797 304" xmlns="http://www.w3.org/2000/svg">
      <!-- wrapper body -->
      <rect class="wrapper-body" x="0" y="0" width="797" height="304" fill="var(--wrapper)"/>

      <!-- top and bottom wave bands -->
      <rect class="wave-band" x="0" y="0" width="797" height="36" fill="var(--green-light)" role="img" aria-label="Green and white wave pattern band"/>
      <rect class="wave-band" x="0" y="270" width="797" height="34" fill="var(--green-light)" role="img" aria-label="Green and white wave pattern band"/>

      <!-- burst ornaments beside the name -->
      <rect class="burst" x="65" y="55" width="124" height="112" rx="10" fill="var(--green-pale)" role="img" aria-label="Hand-drawn green burst lines"/>
      <rect class="burst" x="596" y="55" width="128" height="112" rx="10" fill="var(--green-pale)" role="img" aria-label="Hand-drawn green burst lines"/>

      <!-- name -->
      <text class="brand-name" x="398" y="135" font-size="62" text-anchor="middle">PLUM CRUMB</text>
      <text class="flavour" x="398" y="173" font-size="36" text-anchor="middle">natural</text>

      <!-- benefits stripe -->
      <rect class="benefit-stripe" x="0" y="210" width="797" height="32" fill="var(--green)"/>

      <g class="benefit-badges">
        <rect x="89" y="204" width="124" height="44" rx="9" fill="var(--wrapper)" stroke="var(--green)" stroke-width="2.5"/>
        <text class="badge-label" x="151" y="231" text-anchor="middle">GLUTEN FREE</text>

        <rect x="238" y="204" width="108" height="44" rx="9" fill="var(--wrapper)" stroke="var(--green)" stroke-width="2.5"/>
        <text class="badge-label" x="292" y="231" text-anchor="middle">DIARY FREE</text>

        <rect x="370" y="204" width="72" height="44" rx="9" fill="var(--wrapper)" stroke="var(--green)" stroke-width="2.5"/>
        <text class="badge-label" x="406" y="231" text-anchor="middle">B-12</text>

        <rect x="469" y="204" width="82" height="44" rx="9" fill="var(--wrapper)" stroke="var(--green)" stroke-width="2.5"/>
        <text class="badge-label" x="510" y="231" text-anchor="middle">BIOTIN</text>

        <rect x="582" y="204" width="100" height="44" rx="9" fill="var(--wrapper)" stroke="var(--green)" stroke-width="2.5"/>
        <text class="badge-label" x="632" y="231" text-anchor="middle">COLLAGEN</text>
      </g>
    </svg>
  </div>
</main>
</body>
</html>
```